For lease banners for Businesses

I need to turn all of these banners into high quality graphics so I can get them printed on vinyl vertical banners that are 44"W x 88"H. So I need them most likely to be vector artwork, and ready to upload to a custom vinyl print shop.

```html
<!DOCTYPE html>
<html lang="en">
<head>
<meta charset="utf-8">
<title>Keystone Row Holdings – Leasing Now</title>
<link rel="stylesheet" href="https://fonts.googleapis.com/css2?family=Bebas+Neue&family=Oswald:wght@300;400;500&family=Pinyon+Script&display=swap">
<style>
  :root {
    --ink: #0b0b0a;
    --white: #ffffff;
    --gold: #b9830f;
    --gold-soft: #c48d16;
  }
  * { margin: 0; padding: 0; box-sizing: border-box; }
  html, body { width: 1200px; height: 2400px; overflow: hidden; background: var(--ink); }
  ul { list-style: none; }
  .banner { position: relative; width: 1200px; height: 2400px; overflow: hidden; background: var(--ink); font-family: "Bebas Neue", "Oswald", sans-serif; color: var(--white); }

  .scene-photo {
    position: absolute; inset: 0;
    background:
      radial-gradient(ellipse 420px 300px at 900px 1050px, rgba(120,170,60,.55), transparent 70%),
      radial-gradient(ellipse 500px 380px at 350px 1200px, rgba(150,100,50,.45), transparent 70%),
      radial-gradient(ellipse 700px 500px at 600px 1350px, rgba(70,80,70,.55), transparent 70%),
      radial-gradient(ellipse 600px 500px at 200px 400px, rgba(60,80,40,.35), transparent 70%),
      linear-gradient(180deg, #141a12 0%, #1d2619 35%, #2a3322 55%, #141612 72%, #080808 86%, #050505 100%);
  }
  .scene-shade { position: absolute; left: 0; right: 0; top: 1700px; height: 700px; background: linear-gradient(180deg, transparent, rgba(0,0,0,.75) 30%, #000 100%); }

  .headline { position: absolute; left: 0; width: 1200px; text-align: center; line-height: 1; }
  .headline span { display: block; }
  .headline .line-1 { position: absolute; top: 92px; width: 100%; font-size: 188px; letter-spacing: 1px; }
  .headline .line-2 { position: absolute; top: 262px; width: 100%; font-size: 256px; }
  .headline .line-3 { position: absolute; top: 474px; width: 100%; font-size: 256px; }

  .rule { position: absolute; background: var(--gold); }
  .rule-head { left: 173px; top: 718px; width: 854px; height: 4px; }

  .tagline { position: absolute; top: 742px; left: 0; width: 1200px; text-align: center; font-family: "Pinyon Script", cursive; color: var(--gold-soft); font-size: 104px; line-height: 96px; font-weight: 400; -webkit-text-stroke: 1.5px var(--gold-soft); text-shadow: 0 2px 8px rgba(0,0,0,.6); }

  .features { position: absolute; top: 1495px; left: 38px; width: 1112px; display: flex; }
  .feature { width: 278px; text-align: center; position: relative; }
  .feature + .feature::before { content: ""; position: absolute; left: 0; top: 40px; width: 2px; height: 172px; background: var(--gold); }
  .feature svg { display: block; margin: 0 auto; height: 100px; }
  .feature-label { margin-top: 50px; font-family: "Bebas Neue", sans-serif; font-size: 46px; line-height: 42px; letter-spacing: 1px; }

  .brand { position: absolute; top: 1811px; left: 238px; display: flex; align-items: center; }
  .brand-mark { width: 154px; height: 164px; border: 4px solid var(--gold); }
  .brand-divider { width: 2px; height: 164px; background: var(--gold); margin: 0 42px 0 45px; }
  .brand-name { font-family: "Bebas Neue", sans-serif; color: var(--white); font-size: 86px; line-height: 80px; letter-spacing: 8px; }
  .brand-name small { display: block; font-size: 48px; line-height: 50px; letter-spacing: 17px; }

  .rule-brand { left: 107px; top: 2018px; width: 984px; height: 2px; }
  .rule-foot { left: 107px; top: 2218px; width: 984px; height: 2px; }

  .leasing { position: absolute; left: 107px; top: 2068px; font-size: 112px; line-height: 1; letter-spacing: -1.5px; color: var(--gold); white-space: nowrap; }
  .contact-divider { position: absolute; left: 584px; top: 2055px; width: 2px; height: 128px; background: var(--gold); }
  .contact { position: absolute; left: 624px; font-family: "Oswald", sans-serif; font-weight: 300; font-size: 36px; line-height: 1; display: flex; align-items: center; letter-spacing: -.5px; white-space: nowrap; }
  .contact svg { width: 34px; height: 34px; margin-right: 16px; flex: none; }
  .contact-phone { top: 2072px; }
  .contact-email { top: 2130px; }

  .uses { position: absolute; top: 2240px; left: 0; width: 1200px; height: 70px; font-size: 62px; line-height: 70px; letter-spacing: 4px; }
  .uses span { position: absolute; transform: translateX(-50%); }
  .uses .dot { width: 13px; height: 13px; border-radius: 50%; background: var(--gold); top: 29px; }
</style>
</head>
<body>
<main class="banner">
  <div class="scene-photo" role="img" aria-label="Photo of a group of people meeting around a table with laptops in a warm, plant-filled café"></div>
  <div class="scene-shade"></div>

  <h1 class="headline">
    <span class="line-1">THIS COULD BE</span>
    <span class="line-2">YOUR NEXT</span>
    <span class="line-3">LOCATION.</span>
  </h1>
  <div class="rule rule-head"></div>
  <p class="tagline">Build your business<br>where people gather.</p>

  <ul class="features">
    <li class="feature">
      <svg viewBox="0 0 60 80" fill="none" stroke="var(--gold)" stroke-width="3"><path d="M30 76 C18 58 4 44 4 28 A26 26 0 0 1 56 28 C56 44 42 58 30 76 Z"/><circle cx="30" cy="28" r="10"/></svg>
      <p class="feature-label">HIGH<br>VISIBILITY</p>
    </li>
    <li class="feature">
      <svg viewBox="0 0 130 90" fill="none" stroke="var(--gold)" stroke-width="3"><circle cx="42" cy="14" r="10"/><circle cx="88" cy="14" r="10"/><circle cx="22" cy="42" r="10"/><circle cx="65" cy="42" r="10"/><circle cx="108" cy="42" r="10"/><path d="M26 40 A16 14 0 0 1 58 40"/><path d="M72 40 A16 14 0 0 1 104 40"/><path d="M2 86 V78 A20 18 0 0 1 42 78 V86 M45 86 V78 A20 18 0 0 1 85 78 V86 M88 86 V78 A20 18 0 0 1 128 78 V86 M2 86 H128"/></svg>
      <p class="feature-label">DOWNTOWN<br>TRAFFIC</p>
    </li>
    <li class="feature">
      <svg viewBox="0 0 100 100" fill="none" stroke="var(--gold)" stroke-width="3"><path d="M4 4 H96 V96 H56 V74 H4 Z"/><path d="M12 12 H88 V88 H64 V66 H12 Z"/><rect x="20" y="20" width="20" height="18"/><rect x="48" y="20" width="12" height="12"/><path d="M68 20 V40 H88 M20 50 H40 V62 M50 44 H64 V60"/></svg>
      <p class="feature-label">FLEXIBLE<br>FLOORPLANS</p>
    </li>
    <li class="feature">
      <svg viewBox="0 0 100 100" fill="none" stroke="var(--gold)" stroke-width="3"><circle cx="50" cy="30" r="24"/><path d="M39 30 L47 38 L62 22"/></svg>
      <p class="feature-label">LOCAL<br>OWNERSHIP</p>
    </li>
  </ul>

  <div class="brand">
    <div class="brand-mark"></div>
    <div class="brand-divider"></div>
    <p class="brand-name">KEYSTONE ROW<small>HOLDINGS</small></p>
  </div>

  <div class="rule rule-brand"></div>
  <p class="leasing">LEASING NOW</p>
  <div class="contact-divider"></div>
  <p class="contact contact-phone">
    <svg viewBox="0 0 24 24" fill="var(--gold)"><path d="M6.6 10.8a15.1 15.1 0 0 0 6.6 6.6l2.2-2.2a1 1 0 0 1 1-.25 11.4 11.4 0 0 0 3.6.57 1 1 0 0 1 1 1V20a1 1 0 0 1-1 1A17 17 0 0 1 3 4a1 1 0 0 1 1-1h3.5a1 1 0 0 1 1 1c0 1.25.2 2.450.57 3.57a1 1 0 0 1-.25 1z"/></svg>
    555-014-2290
  </p>
  <p class="contact contact-email">
    <svg viewBox="0 0 24 24" fill="none" stroke="var(--gold)" stroke-width="2"><rect x="2" y="5" width="20" height="14"/><path d="M2 5 L12 13 L22 5 M2 19 L9 11 M22 19 L15 11"/></svg>
    leasing@keystonerowholdings.com
  </p>
  <div class="rule rule-foot"></div>

  <p class="uses">
    <span style="left:287px">RETAIL</span>
    <span class="dot" style="left:403px"></span>
    <span style="left:584px">RESTAURANT</span>
    <span class="dot" style="left:777px"></span>
    <span style="left:910px">OFFICE</span>
  </p>
</main>
</body>
</html>
```